Golf simulator membership club

I need a clean design that associates golf, golfclub, golf simulator. Currently building a golf simulator centre. I need link buttons on top and a short description of the concept on the front page. i have removed the details about booking. Will link to external booking. Maybe also news blog on the right side of the page. Must be responsive to work on PC, iPad, tabs and mobile phone. I have been recommended to ask for WordPress
Industry/Entity Type
Club
Number of Pages Required
1 page
Font styles to use
Sans Serif
Requirements
Must have
- Booking plugin as stated in main description. I have a logo that i have attached.
- Also need a contact form and "meld deg på" form like the one found on my existing homepage tindrift.no

```html
<!DOCTYPE html>
<html lang="no">
<head>
<meta charset="utf-8">
<title>Tindrift – golfsimulatorklubb</title>
<link rel="stylesheet" href="https://fonts.googleapis.com/css2?family=Roboto:wght@400;500;700&display=swap">
<style>
:root{
  --green:#1f6d3b;
  --green-dark:#175630;
  --green-overlay:rgba(31,109,59,.88);
  --orange:#f15a24;
  --grey:#f3f3f3;
  --grey-mid:#e4e4e4;
  --text:#6a6a6a;
  --text-dark:#333;
  --line:#dcdcdc;
  --white:#fff;
}
*{box-sizing:border-box;margin:0;padding:0}
html,body{width:1200px;height:1200px;overflow:hidden;background:#fff}
body{position:relative;font-family:"Roboto",Arial,sans-serif;color:var(--text)}
.screen{position:absolute;background:var(--white);overflow:hidden;box-shadow:0 4px 16px rgba(0,0,0,.2)}
.abs{position:absolute}
.photo-grass{background:linear-gradient(180deg,#cfd5da 0%,#b9c3bd 30%,#7f9f63 52%,#4f7f2d 75%,#3b6a22 100%)}
.photo-coffee{background:linear-gradient(135deg,#3a2414 0%,#7a4e26 35%,#c9a97a 55%,#6b4220 75%,#2f1c0e 100%)}
.photo-sim{background:linear-gradient(180deg,#c6ccd2,#a4ae9c 55%,#6f8f4e)}
.copy{color:var(--text);font-size:6.2px;line-height:10px}
.copy p{margin-bottom:10px}
.m-copy{color:var(--text);font-size:4.6px;line-height:10px}
.m-copy p{margin-bottom:10px}
.link{color:var(--orange);text-decoration:underline}
.btn{position:absolute;background:var(--orange);color:#fff;border-radius:10px;font-weight:500;display:flex;align-items:center;justify-content:center;box-shadow:0 1px 3px rgba(0,0,0,.2)}
.navbar{position:absolute;left:0;right:0;background:var(--green);color:#fff;font-weight:500}
.navbar span{position:absolute}
.brand{position:absolute;display:flex;align-items:center;gap:4px;color:var(--green-dark);font-weight:700}
.brand i{display:block;border-radius:50%;background:var(--green)}
.field{position:absolute;background:#fff;border:1px solid var(--line);color:#999;display:flex;align-items:center;justify-content:space-between;padding:0 4px}
.field b{width:0;height:0;border-left:2px solid transparent;border-right:2px solid transparent;border-top:2px solid #555}
.panel{position:absolute;background:#fff;box-shadow:0 2px 8px rgba(0,0,0,.25)}
.cal{font-size:6px;color:#666}
.cal .head{display:flex;justify-content:space-between;padding:0 12px;margin-bottom:6px;color:#444}
.cal .grid{display:grid;grid-template-columns:repeat(7,1fr);row-gap:3.5px;text-align:center;padding:0 6px}
.cal .dn{color:#444}
.cal .o{color:#bbb}
.cal .sel{background:var(--orange);color:#fff;border-radius:1px}
.news{position:absolute;left:0;width:124px;height:38px;background:#fff;box-shadow:0 1px 3px rgba(0,0,0,.12)}
.news .thumb{position:absolute;left:0;top:0;width:40px;height:38px}
.news .title{position:absolute;left:44px;top:4px;font-size:5.6px;line-height:8px;color:#555}
.news .meta{position:absolute;left:44px;right:4px;top:28px;font-size:5px;color:#777;display:flex;justify-content:space-between;align-items:center}
.news .meta span{display:flex;align-items:center;gap:2px}
.search{position:absolute;background:#fff;border:1px solid var(--line);font-size:5px;color:#999;display:flex;align-items:center;justify-content:space-between;padding:0 5px}
.sidebar{position:absolute;background:var(--grey)}
.side-h{position:absolute;font-size:6px;color:#444}
.steps{position:absolute;font-size:5.8px;line-height:9.5px;color:#666}
.steps p{margin-bottom:9px}
.greenbar{position:absolute;background:var(--green)}
.social{position:absolute;display:flex;flex-direction:column;gap:10px}
.social i{display:block;width:7px;height:7px;border-radius:50%;background:#aaa}
.social i.on{background:var(--orange)}
.hero-text{position:absolute;color:#fff;text-align:center;text-shadow:0 1px 2px rgba(0,0,0,.35)}
.newsletter{position:absolute;background:#fff;border:2px solid var(--green);text-align:center}
.newsletter h4{font-weight:500;color:#444}
.newsletter p{color:#888}
.newsletter .input{margin:0 auto;border-bottom:1px solid var(--line);text-align:left;color:#aaa}
</style>
</head>
<body>

<!-- Mobile: long front page -->
<section class="screen" style="left:48px;top:42px;width:128px;height:1116px">
  <div class="abs" style="left:0;top:0;width:128px;height:34px;background:#eef0f1"></div>
  <div class="brand" style="left:30px;top:12px;font-size:8px"><i style="width:9px;height:9px"></i>tindrift.no</div>
  <div class="navbar" style="top:34px;height:21px">
    <svg class="abs" style="left:7px;top:7px" width="8" height="7"><path d="M0 1h8M0 3.5h8M0 6h8" stroke="#fff" stroke-width="1"/></svg>
  </div>
  <div class="btn" style="left:98px;top:39px;width:24px;height:11px;font-size:4.5px">book</div>
  <div class="abs photo-grass" role="img" aria-label="Golfbane med ball på tee" style="left:0;top:55px;width:128px;height:67px"></div>
  <div class="hero-text" style="left:0;width:128px;top:62px;font-size:8px;font-weight:700;line-height:10px">Døgnåpen golf<br>simulatorklubb</div>
  <div class="hero-text" style="left:8px;width:112px;top:86px;font-size:4.4px;line-height:6px">Snart åpner dørene til første golfsimulatorklubb på Nøtterøy. Kun kr 750,- per mnd for medlemskap med ubegrenset spilletid.</div>
  <div class="abs m-copy" style="left:6px;top:130px;width:116px">
    <p>Vi bygger ut med ny simulator for hvert 15. medlem så her er det førstemann til mølla. Medlemsprisen pr mnd tilsvarer noe over 2 timer spill på andre simulatorsenter i Norge.</p>
    <p>Den lave prisen forutsetter at vi har kontinuitet i medlemsmassen og vi har årsforfall på medlemskapet 1. Desember. Dvs at man tegner seg for et år om gangen slik som i golfklubben. (Noe kortere dette oppstartsåret)</p>
  </div>
  <div class="abs photo-coffee" role="img" aria-label="Kaffekopp i loungen" style="left:0;top:236px;width:128px;height:68px"></div>
  <div class="abs m-copy" style="left:6px;top:312px;width:116px;height:80px;overflow:hidden">Vi har en lounge i klubben hvor det blir sofagrupper, kaffemaskin, snacks og mineralvannsautomat. Vi vil ha en skjerm med Greenkanalen i loungeområdet som forøvrig er på ca. 50 m2. Vi ønsker å lage en trivelig og aktiv klubb her og forutsetter at våre medlemmer er aktive og kommer med forbedringsforslag på alle områder etterhvert som vi kommer godt igang.</div>
  <div class="abs m-copy link" style="left:6px;top:398px">Les mer</div>
  <div class="greenbar" style="left:5px;top:419px;width:118px;height:5px"></div>
  <div class="abs m-copy" style="left:6px;top:432px;width:116px;height:60px;overflow:hidden">Det blir full HD Vertee simulatorer av beste kvalitet og med 120.000 (ja du leste riktig) baner å velge mellom. Lerretet har en størrelse på 4.3 x 3.1m og i full HD kvalitet. Det gir en fantastisk virkelighetsnær presentasjon. Mye grunnet absolutt topp datakapasitet samt HD 1080i prosjektorer.</div>
  <div class="abs m-copy link" style="left:6px;top:498px">Les mer</div>
  <div class="abs m-copy" style="left:6px;top:514px;width:116px;height:120px;overflow:hidden">I FTS spilles det turneringer hver uke hele året og der kan man melde seg på hvis man ønsker det. Der kan man spille mot andre simulatorgolfere fra hele verden. Turneringene starter som oftest søndag og avsluttes søndag så man har en uke på seg til å spille 4 runder. Under runden din så kan du velge en golfer som har spilt en runde (eks et annet medlem fra dagen før) og du får indikasjon på hvor hans eller hennes ball havnet for hvert slag. Gaske fascinerende og artig. Og det er selvfølgelig gratis.</div>
  <div class="abs m-copy" style="left:6px;top:640px;color:#999">Se mer info under <span class="link">Nyheter</span></div>
  <div class="abs m-copy" style="left:6px;top:656px;width:116px;height:32px;overflow:hidden">Vertee simulatorer har 101 sensorer i utslagsmatten som måler bevegelser på køllehodet før tee, treffpunkt på ballen samt ballbanen.</div>
  <div class="abs m-copy link" style="left:6px;top:702px">Les mer</div>
  <div class="abs" style="left:0;top:720px;width:128px;height:90px;background:#fafafa"></div>
  <div class="abs" style="left:60px;top:758px;font-size:9px;font-weight:700;color:rgba(31,109,59,.08)">tindrift.no</div>
  <div class="abs" style="left:6px;top:738px;width:116px;text-align:center;font-size:5px;line-height:9.5px;font-weight:500;color:#333">Vi jobber med den første simulatoren i disse dager og legger ut bilder forløpende når vi har den igang. Se info under "nyheter".</div>
  <div class="btn" style="left:48px;top:784px;width:32px;height:12px;font-size:4.6px">Nyheter</div>
  <div class="abs photo-grass" role="img" aria-label="Golfbane med ball på tee" style="left:0;top:814px;width:128px;height:62px"></div>
  <div class="hero-text" style="left:4px;width:120px;top:834px;font-size:5.4px;line-height:7px">Vi har fått de første påmeldingene. Meld deg på idag for å sikre deg plass</div>
  <div class="hero-text" style="left:4px;width:120px;top:852px;font-size:4px;line-height:6px">Klikk på lenken "Meld deg på nå" nederst på siden</div>
  <div class="abs" style="left:0;top:876px;width:128px;height:130px;background:var(--grey)"></div>
  <div class="newsletter" style="left:8px;top:884px;width:112px;height:110px">
    <h4 style="font-size:5.6px;margin-top:10px">Nyhetsbrev</h4>
    <p style="font-size:4.4px;line-height:8px;margin:8px 6px 0;text-align:left">Abonner på vårt nyhetsbrev og få oppdateringer direkte i innboksen din.</p>
    <div class="input" style="width:98px;font-size:4px;padding:6px 3px;margin-top:6px">Skriv inn e-post adresse</div>
    <div class="btn" style="left:30px;top:80px;width:50px;height:13px;font-size:4.6px;border-radius:3px">Abonnere</div>
  </div>
  <div class="navbar" style="top:1006px;height:110px;font-size:5px">
    <span style="left:26px;top:10px">startsiden</span>
    <span style="left:26px;top:26px">meld deg på nå</span>
    <span style="left:26px;top:41px">kontakt oss</span>
    <span style="left:26px;top:57px">nyheter</span>
    <span style="left:42px;top:98px;font-size:3.6px;font-weight:400;opacity:.7">© 2017 TINDRIFT</span>
  </div>
  <div class="social" style="left:8px;top:1022px;gap:9px"><i style="background:#cfd9d2"></i><i style="background:#cfd9d2"></i><i style="background:#cfd9d2"></i><i style="background:#cfd9d2"></i></div>
</section>

<!-- Desktop front page -->
<section class="screen" style="left:224px;top:82px;width:560px;height:1036px">
  <div class="abs photo-grass" role="img" aria-label="Golfbane med ball på tee og himmel" style="left:0;top:0;width:560px;height:258px"></div>
  <div class="brand" style="left:226px;top:20px;font-size:13px"><i style="width:18px;height:18px"></i>tindrift.no</div>
  <div class="navbar" style="top:58px;height:28px;font-size:5.6px">
    <span style="left:162px;top:11px">startsiden</span>
    <span style="left:226px;top:11px">meld deg på nå</span>
    <span style="left:306px;top:11px">nyheter</span>
    <span style="left:364px;top:11px">kontakt oss</span>
  </div>
  <div class="abs" style="left:0;top:86px;width:560px;height:26px;background:rgba(210,214,216,.85)"></div>
  <div class="abs" style="left:76px;top:96px;font-size:5.6px;color:#555">Dato:</div>
  <div class="field" style="left:102px;top:92px;width:82px;height:14px;font-size:5px;border-color:var(--orange)">- 1 februar 2016 -<b></b></div>
  <div class="abs" style="left:206px;top:96px;font-size:5.6px;color:#555">tid:</div>
  <div class="field" style="left:228px;top:92px;width:80px;height:14px;font-size:5px">- 14:00 - 16:00 -<b></b></div>
  <div class="abs" style="left:332px;top:96px;font-size:5.6px;color:#555">Simulator:</div>
  <div class="field" style="left:376px;top:92px;width:76px;height:14px;font-size:5px">- Simulator 1 -<b></b></div>
  <div class="btn" style="left:478px;top:92px;width:36px;height:15px;font-size:5.4px">book</div>

  <div class="hero-text" style="left:0;width:560px;top:200px;font-size:14px;line-height:17px;font-weight:300;opacity:.9">750 pr mnd for medlemskap med<br>ubegrenset spilletid</div>

  <div class="panel cal" style="left:74px;top:114px;width:122px;height:100px;padding-top:10px">
    <div class="head"><span>‹</span><span>februar 2016</span><span>›</span></div>
    <div class="grid">
      <span class="dn">Ma</span><span class="dn">Ti</span><span class="dn">On</span><span class="dn">To</span><span class="dn">Fr</span><span class="dn">Lø</span><span class="dn">Sø</span>
      <span class="o">31</span><span>1</span><span>2</span><span>3</span><span>4</span><span>5</span><span>6</span>
      <span>7</span><span>8</span><span>9</span><span>10</span><span>11</span><span>12</span><span>13</span>
      <span>14</span><span>15</span><span>16</span><span>17</span><span>18</span><span>19</span><span>20</span>
      <span>21</span><span>22</span><span>23</span><span class="sel">24</span><span>25</span><span>26</span><span>27</span>
      <span>28</span><span class="o">1</span><span class="o">2</span><span class="o">3</span><span class="o">4</span><span class="o">5</span><span class="o">6</span>
    </div>
  </div>

  <div class="panel" style="left:200px;top:114px;width:120px;height:92px;font-size:5.8px;color:#555">
    <div class="abs" style="left:10px;top:40px">Fra:</div>
    <div class="abs" style="left:68px;top:40px">Til:</div>
    <div class="abs" style="left:30px;top:8px;width:24px;text-align:center;line-height:10px">˄<br>08:00<br>08:30<br><span style="display:block;background:var(--grey-mid)">09:00</span>09:30<br>˅</div>
    <div class="abs" style="left:86px;top:8px;width:24px;text-align:center;line-height:10px">˄<br>08:00<br><span style="display:block;background:var(--grey-mid)">08:30</span>09:00<br>09:30<br>˅</div>
  </div>

  <div class="panel" style="left:326px;top:114px;width:140px;height:92px;font-size:5.6px;color:#555">
    <div class="abs" style="left:8px;top:8px;width:58px;line-height:11.6px;border:1px solid var(--line);padding:0 4px">Simulator 1<br>Simulator 2<br><span style="display:block;margin:0 -4px;padding:0 4px;background:#ccc;color:#fff">Simulator 3</span>Simulator 4<br>Simulator 5<br>Simulator 6</div>
    <div class="abs photo-sim" role="img" aria-label="Bilde av valgt simulator" style="left:70px;top:6px;width:58px;height:78px"></div>
    <div class="abs" style="left:70px;top:32px;width:58px;text-align:center;font-size:8px;font-weight:700;color:#fff;line-height:10px;opacity:.85">Simulator<br>Picture</div>
  </div>

  <div class="sidebar" style="left:366px;top:258px;width:194px;height:540px"></div>
  <div class="abs copy" style="left:46px;top:282px;width:250px">
    <p>Vi bygger ut med ny simulator for hvert 15. medlem så her er det førstemann til mølla. Medlemsprisen pr.mnd tilsvarer noe over 2 timer spill på andre simulatorsenter i Norge.</p>
    <p>Den lave prisen forutsetter at vi har kontinuitet i medlemsmassen og vi har årsforfall på medlemskapet 1. Desember. Dvs at man tegner seg for et år om gangen slik som i golfklubben. (Noe kortere dette oppstartsåret)</p>
  </div>
  <div class="brand" style="left:290px;top:318px;font-size:9px"><i style="width:12px;height:12px"></i>tindrift.no</div>
  <div class="abs photo-coffee" role="img" aria-label="Kaffekopp i loungen" style="left:46px;top:385px;width:92px;height:109px"></div>
  <div class="abs copy" style="left:150px;top:386px;width:204px">Vi har en lounge i klubben hvor det blir sofagrupper, kaffemaskin, snacks og mineralvannsautomat. Vi vil ha en skjerm med Greenkanalen i loungeområdet som forøvrig er på ca. 50 m2. Vi ønsker å lage en trivelig og aktiv klubb her og forutsetter at våre medlemmer er aktive og kommer med forbedringsforslag på alle områder etterhvert som vi kommer godt igang. Vi skal jobbe for å få til den gode klubbfølelsen hvor medlemmene kan møtes, spille golf, se på golf i loungen og ha det hyggelig. Dette tror vi kommer til å bli helt topp både i store deler av vinterhalvåret samt på kjølige eller regnfulle vår, sommer eller høstdager. Eller når hjemmebanen har turnering, er fullbooket eller stengt. Husk at vi alle har tilgang til senteret 24/7.</div>

  <div class="abs" style="left:0;top:522px;width:366px;height:276px;background:#fafafa"></div>
  <div class="greenbar" style="left:46px;top:544px;width:148px;height:6px"></div>
  <div class="abs copy" style="left:46px;top:564px;width:148px">
    <p>Det blir full HD Vertee simulatorer av beste kvalitet og med 120.000 (ja du leste riktig) baner å velge mellom. Lerretet har en størrelse på 4.3 x 3.1m og i full HD kvalitet. Det gir en fantastisk virkelighetsnær presentasjon. Mye grunnet absolutt topp datakapasitet samt HD 1080i prosjektorer av type Short Throw som sitter nærme lerretet og gir en helt utrolig opplevelse. I tillegg slipper man skygge på lerretet (både ved teeshots og putting). Vi har ikke sett alle simulatorer i Norge men ingen av de vi har sett er i nærheten av den samme kvaliteten på bildet som vi får her i klubben.</p>
    <p>Softwaren vi kjører er FTS (Fairway Tour Suite) som sammen med sensorer og kameraer i systemet gir en utrolig nøyaktig analyse av hvert slag og det presenteres på en veldig oversiktlig måte på skjermen rett etter slaget. Du kan hente ut all slags statistikker på deg selv og hvordan du har spilt når du har gått noen runder på simulatoren.</p>
  </div>
  <div class="abs copy" style="left:206px;top:544px;width:148px">
    <p>I FTS spilles det turneringer hver uke hele året og der kan man melde seg på hvis man ønsker det. Der kan man spille mot andre simulatorgolfere fra hele verden. Turneringene starter som oftest søndag og avsluttes søndag så man har en uke på seg til å spille 4 runder. Under runden din så kan du velge en golfer som har spilt en runde (eks et annet medlem fra dagen før) og du får indikasjon på hvor hans eller hennes ball havnet for hvert slag. Gaske fascinerende og artig. Og det er selvfølgelig gratis.</p>
    <p style="color:#999">Se mer info under <span class="link">Nyheter</span></p>
    <p>Vertee simulatorer har 101 sensorer i utslagsmatten som måler bevegelser på køllehodet før tee, treffpunkt på ballen samt ballbanen. I tillegg sitter det 2 High speed kameraer som måler ballbanen hhv horisontalt og vertikalt. Der egen innfelt putting sensor matte er plassert en mtr foran utslagssensoren (også i senter av lerret) og gir en meget nøyaktig måling på putt. Antageligvis den mest virkelighetsnære puttingen mulig på simulator idag.</p>
  </div>
  <div class="social" style="left:7px;top:612px"><i></i><i class="on"></i><i></i><i></i></div>
  <div class="abs" style="left:6px;top:686px;width:9px;height:9px;border:1px solid #bbb;border-radius:50%"></div>

  <div class="search" style="left:378px;top:282px;width:124px;height:14px">søk nyheter
    <svg width="6" height="6"><circle cx="2.5" cy="2.5" r="1.8" fill="none" stroke="#555" stroke-width=".8"/><path d="M4 4l1.8 1.8" stroke="#555" stroke-width=".8"/></svg></div>
  <div class="side-h" style="left:378px;top:322px">Siste nytt</div>
  <div class="abs" style="left:378px;top:340px;width:124px;height:120px">
    <div class="news" style="top:0"><div class="thumb photo-grass" role="img" aria-label="Golfbane"></div><div class="title">Se presentasjon av<br>software og hardware</div><div class="meta"><span><svg width="5" height="5"><rect x=".5" y="1" width="4" height="3.5" fill="none" stroke="#777" stroke-width=".6"/></svg>02/27/2017</span><span><svg width="7" height="5"><ellipse cx="3.5" cy="2.5" rx="3" ry="2" fill="none" stroke="#333" stroke-width=".7"/><circle cx="3.5" cy="2.5" r="1" fill="#333"/></svg>10</span></div></div>
    <div class="news" style="top:40px"><div class="thumb photo-grass" role="img" aria-label="Golfbane"></div><div class="title">Se presentasjon av<br>software og hardware</div><div class="meta"><span><svg width="5" height="5"><rect x=".5" y="1" width="4" height="3.5" fill="none" stroke="#777" stroke-width=".6"/></svg>02/27/2017</span><span><svg width="7" height="5"><ellipse cx="3.5" cy="2.5" rx="3" ry="2" fill="none" stroke="#333" stroke-width=".7"/><circle cx="3.5" cy="2.5" r="1" fill="#333"/></svg>10</span></div></div>
    <div class="news" style="top:80px"><div class="thumb photo-grass" role="img" aria-label="Golfbane"></div><div class="title">Se presentasjon av<br>software og hardware</div><div class="meta"><span><svg width="5" height="5"><rect x=".5" y="1" width="4" height="3.5" fill="none" stroke="#777" stroke-width=".6"/></svg>02/27/2017</span><span><svg width="7" height="5"><ellipse cx="3.5" cy="2.5" rx="3" ry="2" fill="none" stroke="#333" stroke-width=".7"/><circle cx="3.5" cy="2.5" r="1" fill="#333"/></svg>10</span></div></div>
  </div>
  <div class="btn" style="left:434px;top:471px;width:64px;height:16px;font-size:5.4px">se alle nyheter</div>
  <div class="side-h" style="left:378px;top:502px">Slik er prosessen:</div>
  <div class="steps" style="left:378px;top:520px;width:124px">
    <p>1. Meld din interesse her på siden via kontaktskjema, ikke forpliktende!</p>
    <p>2. Vi sender kontrakt på email til deg, du signerer og returnerer til oss.</p>
  </div>

  <div class="abs" style="left:0;top:798px;width:560px;height:86px;background:#fafafa"></div>
  <div class="abs" style="left:174px;top:840px;font-size:22px;font-weight:700;color:rgba(31,109,59,.08)">tindrift.no</div>
  <div class="abs" style="left:0;width:560px;top:820px;text-align:center;font-size:5.8px;line-height:10px;font-weight:500;color:#333">Vi jobber med den første simulatoren i disse dager og legger ut bilder fortløpende<br>når vi har den igang. Se info under "nyheter".</div>
  <div class="btn" style="left:230px;top:851px;width:44px;height:15px;font-size:5.6px">Nyheter</div>
  <div class="abs photo-grass" role="img" aria-label="Golfbane med ball på tee" style="left:0;top:884px;width:560px;height:102px"></div>
  <div class="hero-text" style="left:0;width:560px;top:906px;font-size:13px;line-height:16px;font-weight:300">Vi har fått de første påmeldingene. Meld<br>deg på idag for å sikre deg plass</div>
  <div class="hero-text" style="left:0;width:560px;top:950px;font-size:7.5px">Klikk på lenken "Meld deg på nå" nederst på siden</div>
  <div class="navbar" style="top:986px;height:32px;font-size:5.6px">
    <span style="left:162px;top:13px">startsiden</span>
    <span style="left:226px;top:13px">meld deg på nå</span>
    <span style="left:306px;top:13px">nyheter</span>
    <span style="left:364px;top:13px">kontakt oss</span>
  </div>
  <div class="abs" style="left:0;top:1018px;width:560px;height:18px;background:var(--green-dark);color:#cfe0d4;font-size:4.6px;text-align:center;line-height:18px">© 2017 TINDRIFT</div>
</section>

<!-- Mobile: date picker open -->
<section class="screen" style="left:822px;top:42px;width:128px;height:276px">
  <div class="navbar" style="top:0;height:20px">
    <svg class="abs" style="left:7px;top:7px" width="8" height="7"><path d="M0 1h8M0 3.5h8M0 6h8" stroke="#fff" stroke-width="1"/></svg>
  </div>
  <div class="btn" style="left:98px;top:4px;width:22px;height:11px;font-size:4.4px">book</div>
  <div class="abs photo-grass" role="img" aria-label="Golfbane" style="left:0;top:20px;width:128px;height:20px"></div>
  <div class="abs" style="left:22px;top:27px;font-size:4.6px;color:#444">Dato:</div>
  <div class="field" style="left:40px;top:24px;width:78px;height:11px;font-size:4.2px">- 1 februar 2016 -<b></b></div>
  <div class="abs m-copy" style="left:4px;top:138px;width:118px">
    <p>medlem så her er det førstemann til mølla. Medlemsprisen pr mnd tilsvarer noe over 2 timer spill på andre simulatorsenter i Norge.</p>
    <p>Den lave prisen forutsetter at vi har kontinuitet i medlemsmassen og vi har årsforfall på medlemskapet 1. Desember. Dvs at man tegner seg for et år om gangen slik som i golfklubben. (Noe kortere dette oppstartsåret)</p>
  </div>
  <div class="abs photo-coffee" role="img" aria-label="Kaffekopp i loungen" style="left:0;top:236px;width:128px;height:40px"></div>
  <div class="panel cal" style="left:2px;top:40px;width:124px;height:102px;padding-top:10px;font-size:5.6px">
    <div class="head"><span>‹</span><span>februar 2016</span><span>›</span></div>
    <div class="grid">
      <span class="dn">Ma</span><span class="dn">Ti</span><span class="dn">On</span><span class="dn">To</span><span class="dn">Fr</span><span class="dn">Lø</span><span class="dn">Sø</span>
      <span class="o">31</span><span>1</span><span>2</span><span>3</span><span>4</span><span>5</span><span>6</span>
      <span>7</span><span>8</span><span>9</span><span>10</span><span>11</span><span>12</span><span>13</span>
      <span>14</span><span>15</span><span>16</span><span>17</span><span>18</span><span>19</span><span>20</span>
      <span>21</span><span>22</span><span>23</span><span class="sel">24</span><span>25</span><span>26</span><span>27</span>
      <span>28</span><span class="o">1</span><span class="o">2</span><span class="o">3</span><span class="o">4</span><span class="o">5</span><span class="o">6</span>
    </div>
  </div>
</section>

<!-- Mobile: menu open -->
<section class="screen" style="left:1006px;top:42px;width:128px;height:270px;background:var(--grey)">
  <div class="abs photo-grass" role="img" aria-label="Golfbane" style="left:0;top:0;width:128px;height:152px"></div>
  <div class="navbar" style="top:0;height:20px">
    <svg class="abs" style="left:8px;top:6px" width="7" height="8"><path d="M1 0v8M3.5 0v8M6 0v8" stroke="#fff" stroke-width="1"/></svg>
  </div>
  <div class="btn" style="left:98px;top:4px;width:24px;height:11px;font-size:4.4px">book</div>
  <div class="abs" style="left:0;top:20px;width:128px;height:100px;background:var(--green-overlay)"></div>
  <div class="search" style="left:6px;top:28px;width:116px;height:13px;font-size:4.4px">søk nyheter
    <svg width="6" height="6"><circle cx="2.5" cy="2.5" r="1.8" fill="none" stroke="#555" stroke-width=".8"/><path d="M4 4l1.8 1.8" stroke="#555" stroke-width=".8"/></svg></div>
  <div class="abs" style="left:12px;top:60px;font-size:5px;line-height:15.5px;font-weight:500;color:#fff">startsiden<br>meld deg på nå<br>kontakt oss<br>nyheter</div>
  <div class="abs" style="left:50px;top:61px;width:30px;height:9px;border-radius:5px;background:rgba(255,255,255,.2);font-size:3.4px;color:#dfe;text-align:center;line-height:9px">Nyheter</div>
  <div class="hero-text" style="left:4px;width:120px;top:130px;font-size:4px;line-height:6px">Klikk på lenken "Meld deg på nå" nederst på siden</div>
  <div class="newsletter" style="left:8px;top:162px;width:112px;height:108px;border-bottom:none">
    <h4 style="font-size:5.6px;margin-top:9px">Nyhetsbrev</h4>
    <p style="font-size:4.4px;line-height:8px;margin:8px 6px 0;text-align:left">Abonner på vårt nyhetsbrev og få oppdateringer direkte i innboksen din.</p>
    <div class="input" style="width:98px;font-size:4px;padding:6px 3px;margin-top:6px">Skriv inn e-post adresse</div>
    <div class="btn" style="left:30px;top:80px;width:50px;height:13px;font-size:4.6px;border-radius:3px">Abonnere</div>
  </div>
</section>

<!-- Mobile: booking form -->
<section class="screen" style="left:898px;top:300px;width:128px;height:272px">
  <div class="abs photo-grass" role="img" aria-label="Golfbane med ball på tee" style="left:0;top:20px;width:128px;height:104px"></div>
  <div class="navbar" style="top:0;height:20px">
    <svg class="abs" style="left:7px;top:7px" width="8" height="7"><path d="M0 1h8M0 3.5h8M0 6h8" stroke="#fff" stroke-width="1"/></svg>
  </div>
  <div class="btn" style="left:98px;top:4px;width:22px;height:11px;font-size:4.4px">book</div>
  <div class="abs" style="left:0;top:20px;width:128px;height:52px;background:rgba(215,218,220,.85)"></div>
  <div class="abs" style="left:0;width:36px;top:28px;text-align:right;font-size:4.4px;line-height:16.5px;color:#444">Dato:<br>tid:<br>Simulator:</div>
  <div class="field" style="left:40px;top:26px;width:78px;height:10px;font-size:4px">- 1 februar 2016 -<b></b></div>
  <div class="field" style="left:40px;top:42px;width:78px;height:10px;font-size:4px">- 14:00 - 16:00 -<b></b></div>
  <div class="field" style="left:40px;top:59px;width:78px;height:10px;font-size:4px">- Simulator 1 -<b></b></div>
  <div class="hero-text" style="left:0;width:128px;top:74px;font-size:8px;font-weight:700">simulatorklubb</div>
  <div class="btn" style="left:52px;top:78px;width:24px;height:10px;font-size:4.2px">book</div>
  <div class="hero-text" style="left:8px;width:112px;top:92px;font-size:4.2px;line-height:6px">Kun kr 750,- per mnd for medlemskap med ubegrenset spilletid.</div>
  <div class="abs m-copy" style="left:4px;top:130px;width:118px">
    <p>Vi bygger ut med ny simulator for hvert 15. medlem så her er det førstemann til mølla. Medlemsprisen pr mnd tilsvarer noe over 2 timer spill på andre simulatorsenter i Norge.</p>
    <p>Den lave prisen forutsetter at vi har kontinuitet i medlemsmassen og vi har årsforfall på medlemskapet 1. Desember. Dvs at man tegner seg for et år om gangen slik som i golfklubben. (Noe kortere dette oppstartsåret)</p>
  </div>
  <div class="abs photo-coffee" role="img" aria-label="Kaffekopp i loungen" style="left:0;top:234px;width:128px;height:38px"></div>
</section>

<!-- Tablet: scrolled page with sticky menu -->
<section class="screen" style="left:592px;top:665px;width:560px;height:535px">
  <div class="sidebar" style="left:368px;top:0;width:192px;height:535px"></div>
  <div class="abs copy" style="left:46px;top:26px;width:240px">
    <p>Vi bygger ut med ny simulator for hvert 15. medlem så her er det førstemann til mølla. Medlemsprisen pr.mnd tilsvarer noe over 2 timer spill på andre simulatorsenter i Norge.</p>
    <p>Den lave prisen forutsetter at vi har kontinuitet i medlemsmassen og vi har årsforfall på medlemskapet 1. Desember. Dvs at man tegner seg for et år om gangen slik som i golfklubben. (Noe kortere dette oppstartsåret)</p>
  </div>
  <div class="brand" style="left:290px;top:58px;font-size:9px"><i style="width:12px;height:12px"></i>tindrift.no</div>
  <div class="abs photo-coffee" role="img" aria-label="Kaffekopp i loungen" style="left:46px;top:127px;width:92px;height:110px"></div>
  <div class="abs copy" style="left:150px;top:128px;width:206px">Vi har en lounge i klubben hvor det blir sofagrupper, kaffemaskin, snacks og mineralvannsautomat. Vi vil ha en skjerm med Greenkanalen i loungeområdet som forøvrig er på ca. 50 m2. Vi ønsker å lage en trivelig og aktiv klubb her og forutsetter at våre medlemmer er aktive og kommer med forbedringsforslag på alle områder etterhvert som vi kommer godt igang. Vi skal jobbe for å få til den gode klubbfølelsen hvor medlemmene kan møtes, spille golf, se på golf i loungen og ha det hyggelig. Dette tror vi kommer til å bli helt topp både i store deler av vinterhalvåret samt på kjølige eller regnfulle vår, sommer eller høstdager. Eller når hjemmebanen har turnering, er fullbooket eller stengt. Husk at vi alle har tilgang til senteret 24/7.</div>
  <div class="abs" style="left:0;top:266px;width:368px;height:269px;background:#fafafa"></div>
  <div class="greenbar" style="left:46px;top:286px;width:148px;height:6px"></div>
  <div class="abs copy" style="left:46px;top:306px;width:148px">
    <p>Det blir full HD Vertee simulatorer av beste kvalitet og med 120.000 (ja du leste riktig) baner å velge mellom. Lerretet har en størrelse på 4.3 x 3.1m og i full HD kvalitet. Det gir en fantastisk virkelighetsnær presentasjon. Mye grunnet absolutt topp datakapasitet samt HD 1080i prosjektorer av type Short Throw som sitter nærme lerretet og gir en helt utrolig opplevelse. I tillegg slipper man skygge på lerretet (både ved teeshots og putting). Vi har ikke sett alle simulatorer i Norge men ingen av de vi har sett er i nærheten av den samme kvaliteten på bildet som vi får her i klubben.</p>
    <p>Softwaren vi kjører er FTS (Fairway Tour Suite) som sammen med sensorer og kameraer i systemet gir en utrolig nøyaktig analyse av hvert slag og det presenteres på en veldig oversiktlig måte på skjermen rett etter slaget. Du kan hente ut all slags statistikker på deg selv og hvordan du har spilt når du har gått noen runder på simulatoren.</p>
  </div>
  <div class="abs copy" style="left:206px;top:286px;width:150px">
    <p>I FTS spilles det turneringer hver uke hele året og der kan man melde seg på hvis man ønsker det. Der kan man spille mot andre simulatorgolfere fra hele verden. Turneringene starter som oftest søndag og avsluttes søndag så man har en uke på seg til å spille 4 runder. Under runden din så kan du velge en golfer som har spilt en runde (eks et annet medlem fra dagen før) og du får indikasjon på hvor hans eller hennes ball havnet for hvert slag. Gaske fascinerende og artig. Og det er selvfølgelig gratis.</p>
    <p style="color:#999">Se mer info under <span class="link">Nyheter</span></p>
    <p>Vertee simulatorer har 101 sensorer i utslagsmatten som måler bevegelser på køllehodet før tee, treffpunkt på ballen samt ballbanen. I tillegg sitter det 2 High speed kameraer som måler ballbanen hhv horisontalt og vertikalt. Der egen innfelt putting sensor matte er plassert en mtr foran utslagssensoren (også i senter av lerret) og gir en meget nøyaktig måling på putt. Antageligvis den mest virkelighetsnære puttingen mulig på simulator idag.</p>
  </div>
  <div class="social" style="left:9px;top:356px"><i></i><i class="on"></i><i></i><i></i></div>
  <div class="abs" style="left:8px;top:430px;width:9px;height:9px;border:1px solid #bbb;border-radius:50%"></div>

  <div class="search" style="left:378px;top:26px;width:124px;height:14px">søk nyheter
    <svg width="6" height="6"><circle cx="2.5" cy="2.5" r="1.8" fill="none" stroke="#555" stroke-width=".8"/><path d="M4 4l1.8 1.8" stroke="#555" stroke-width=".8"/></svg></div>
  <div class="side-h" style="left:378px;top:64px">Siste nytt</div>
  <div class="abs" style="left:378px;top:81px;width:124px;height:120px">
    <div class="news" style="top:0"><div class="thumb photo-grass" role="img" aria-label="Golfbane"></div><div class="title">Se presentasjon av<br>software og hardware</div><div class="meta"><span><svg width="5" height="5"><rect x=".5" y="1" width="4" height="3.5" fill="none" stroke="#777" stroke-width=".6"/></svg>02/27/2017</span><span><svg width="7" height="5"><ellipse cx="3.5" cy="2.5" rx="3" ry="2" fill="none" stroke="#333" stroke-width=".7"/><circle cx="3.5" cy="2.5" r="1" fill="#333"/></svg>10</span></div></div>
    <div class="news" style="top:40px"><div class="thumb photo-grass" role="img" aria-label="Golfbane"></div><div class="title">Se presentasjon av<br>software og hardware</div><div class="meta"><span><svg width="5" height="5"><rect x=".5" y="1" width="4" height="3.5" fill="none" stroke="#777" stroke-width=".6"/></svg>02/27/2017</span><span><svg width="7" height="5"><ellipse cx="3.5" cy="2.5" rx="3" ry="2" fill="none" stroke="#333" stroke-width=".7"/><circle cx="3.5" cy="2.5" r="1" fill="#333"/></svg>10</span></div></div>
    <div class="news" style="top:80px"><div class="thumb photo-grass" role="img" aria-label="Golfbane"></div><div class="title">Se presentasjon av<br>software og hardware</div><div class="meta"><span><svg width="5" height="5"><rect x=".5" y="1" width="4" height="3.5" fill="none" stroke="#777" stroke-width=".6"/></svg>02/27/2017</span><span><svg width="7" height="5"><ellipse cx="3.5" cy="2.5" rx="3" ry="2" fill="none" stroke="#333" stroke-width=".7"/><circle cx="3.5" cy="2.5" r="1" fill="#333"/></svg>10</span></div></div>
  </div>
  <div class="btn" style="left:434px;top:214px;width:64px;height:16px;font-size:5.4px">se alle nyheter</div>
  <div class="side-h" style="left:378px;top:246px">Slik er prosessen:</div>
  <div class="steps" style="left:378px;top:264px;width:126px">
    <p>1. Meld din interesse her på siden via kontaktskjema, ikke forpliktende!</p>
    <p>2. Vi sender kontrakt på email til deg, du signerer og returnerer til oss.</p>
    <p>3. Du betaler en innmeldingsavgift på 500,- samt første mnd medlemsavgift. Dette skal skje en uke før simulatoren er spilleklar. Dette for å forberede brukerprofil og kode/kodebrikke for adgang til senteret.</p>
    <p>3. Du mottar en kode/kodebrikke til senteret og kan starte booking av timer på hvilken som helst ledig simulator i senteret via booking appen og/eller hjemmesiden.</p>
    <p>4. Senteret er åpent 24/7/365 og kun unntaksvis bemannet.</p>
  </div>
  <div class="btn" style="left:442px;top:466px;width:56px;height:15px;font-size:5.4px">kontakt oss</div>
  <div class="newsletter" style="left:378px;top:494px;width:124px;height:60px">
    <h4 style="font-size:8.5px;margin-top:9px">Nyhetsbrev</h4>
    <p style="font-size:4.6px;margin-top:8px">Abonner på vårt nyhetsbrev og få</p>
  </div>

  <div class="navbar" style="top:0;height:30px;font-size:5.6px;box-shadow:0 1px 4px rgba(0,0,0,.25)">
    <span style="left:176px;top:12px">startsiden</span>
    <span style="left:226px;top:12px">meld deg på nå</span>
    <span style="left:318px;top:12px">nyheter</span>
    <span style="left:366px;top:12px">kontakt oss</span>
  </div>
  <div class="btn" style="left:478px;top:7px;width:36px;height:15px;font-size:5.4px">book</div>
</section>

</body>
</html>
```